Financial Coaching & Personal Development

I’m desiring a classic business card for my financial coaching and personal development business. The colors I have started with are a goldish brown and hunter green. The brownish color represents soil and green represents growth. I don’t want it it to look masculine. I want the brown to be more of a golden color. I want the color combination and overall design to be timeless not trendy. The logo can be changed as long as it represents growth- moving from where you are to where you want to be.

Target Market(s)

Working Adults with median income $65k; small businesses with a minimum of 20 employees

Industry/Entity Type

Consulting

Contact Information for Business Card

Marla Quenby, MBA
Certified Financial Coach

Font styles to use
Serif

Requirements
Must have
• Logo
My name
Business description
Email marla.quenby@thrivelanefundhouse
Phone number 662-555-0187
Nice to have
• Slogan

```html
<!DOCTYPE html>
<html lang="en">
<head>
<meta charset="utf-8">
<title>Thrivelane Fund House – Business Card</title>
<link href="https://fonts.googleapis.com/css2?family=Arimo:wght@400;700&family=Tinos&family=Pinyon+Script&display=swap" rel="stylesheet">
<style>
  :root {
    --backdrop: #141414;
    --card: #2b2c2e;
    --card-edge: #2f9a1f;
    --gold: #7d5f12;
    --green: #2e9c1b;
    --ink-light: #f2f2f2;
    --rule: #6b6b6b;
    --emboss: #3a3b3e;
  }
  * { margin: 0; padding: 0; box-sizing: border-box; }
  html, body { width: 1200px; height: 820px; overflow: hidden; }
  body {
    background: var(--backdrop);
    display: flex;
    align-items: center;
    justify-content: center;
    gap: 50px;
    font-family: "Arimo", sans-serif;
  }
  .card {
    position: relative;
    width: 540px;
    height: 310px;
    background: var(--card);
    border-left: 3px solid var(--card-edge);
    border-bottom: 3px solid var(--card-edge);
    box-shadow: 0 18px 40px rgba(0,0,0,.6);
    overflow: hidden;
  }

  /* Front */
  .brand {
    position: absolute;
    top: 58px;
    right: 50px;
    text-align: center;
    width: 300px;
  }
  .brand__mark {
    display: inline-block;
    width: 22px; height: 22px;
    border-radius: 50%;
    background: var(--green);
    margin-bottom: 10px;
  }
  .brand__name {
    font-weight: 700;
    font-size: 19px;
    letter-spacing: 1.5px;
    color: var(--gold);
    text-transform: uppercase;
  }
  .brand__tagline {
    font-family: "Tinos", serif;
    font-size: 11px;
    color: var(--green);
    margin-top: 3px;
  }
  .divider {
    position: absolute;
    left: 250px;
    right: 40px;
    top: 170px;
    border-top: 1px solid var(--rule);
  }
  .person {
    position: absolute;
    left: 40px;
    top: 150px;
  }
  .person__name {
    font-weight: 700;
    font-size: 19px;
    color: var(--gold);
    text-transform: uppercase;
  }
  .person__creds { color: var(--green); }
  .person__title {
    font-size: 16px;
    color: var(--ink-light);
    margin-top: 2px;
  }
  .contacts {
    position: absolute;
    left: 40px;
    top: 218px;
    list-style: none;
    font-size: 14px;
    color: var(--ink-light);
  }
  .contacts li {
    display: flex;
    align-items: center;
    gap: 8px;
    margin-bottom: 5px;
  }
  .contacts svg { width: 14px; height: 14px; fill: var(--gold); flex: none; }
  .contacts .web-domain { color: var(--green); }

  /* Back */
  .back__brand {
    position: absolute;
    left: 30px;
    top: 128px;
    width: 280px;
    text-align: center;
    font-weight: 700;
    font-size: 26px;
    letter-spacing: 2px;
    text-transform: uppercase;
    color: var(--emboss);
  }
  .slogan {
    position: absolute;
    right: 30px;
    top: 62px;
    width: 190px;
    font-family: "Pinyon Script", cursive;
    font-size: 31px;
    line-height: 38px;
    color: var(--green);
    text-align: center;
  }
</style>
</head>
<body>

  <section class="card card--front">
    <div class="brand">
      <span class="brand__mark"></span>
      <div class="brand__name">Thrivelane Fund House</div>
      <div class="brand__tagline">Financial Education &amp; Personal Development</div>
    </div>

    <div class="divider"></div>

    <div class="person">
      <div class="person__name">Marla Quenby, <span class="person__creds">MBA</span></div>
      <div class="person__title">Certified Financial Coach</div>
    </div>

    <ul class="contacts">
      <li>
        <svg viewBox="0 0 24 24" aria-hidden="true"><path d="M6.6 10.8a15.1 15.1 0 0 0 6.6 6.6l2.2-2.2a1 1 0 0 1 1-.25 11.4 11.4 0 0 0 3.6.57 1 1 0 0 1 1 1V20a1 1 0 0 1-1 1A17 17 0 0 1 3 4a1 1 0 0 1 1-1h3.5a1 1 0 0 1 1 1c0 1.25.2 2.45.57 3.57a1 1 0 0 1-.25 1z"/></svg>
        662-555-0187
      </li>
      <li>
        <svg viewBox="0 0 24 24" aria-hidden="true"><path d="M2 5h20v14H2zm2 2v.5l8 5 8-5V7l-8 5z"/></svg>
        marla.quenby@thrivelanefundhouse.com
      </li>
      <li>
        <svg viewBox="0 0 24 24" aria-hidden="true"><path d="M12 2a10 10 0 1 0 0 20 10 10 0 0 0 0-20zm0 2c.9 0 2.2 1.8 2.8 5H9.2C9.8 5.8 11.1 4 12 4zM4.3 9h3A18 18 0 0 0 7 12c0 1 .1 2 .3 3h-3a8 8 0 0 1 0-6zm5 6a16 16 0 0 1 0-6h5.4a16 16 0 0 1 0 6zm7.4 0c.2-1 .3-2 .3-3s-.1-2-.3-3h3a8 8 0 0 1 0 6zM12 20c-.9 0-2.2-1.8-2.8-5h5.6c-.6 3.2-1.9 5-2.8 5z"/></svg>
        <span>www.<span class="web-domain">thrivelanefundhouse</span>.com</span>
      </li>
    </ul>
  </section>

  <section class="card card--back">
    <div class="back__brand">Thrivelane Fund House</div>
    <p class="slogan">Create a Financial Plan that makes you Smile!</p>
  </section>

</body>
</html>
```